Quolvex custom business card design

Need a authentic, innovative business card design for a new mobile app business. I am uploading a few screen images from our app for you to view. I would like app design theme to match business card design. I can also send logo images.

```html
<!DOCTYPE html>
<html lang="en">
<head>
<meta charset="UTF-8">
<title>Quolvex Business Card</title>
<link rel="stylesheet" href="https://fonts.googleapis.com/css2?family=Montserrat:wght@400;700;800&family=Open+Sans:wght@400&display=swap">
<style>
  :root {
    --stage: #2b2b2d;
    --card-dark: #1c1c1e;
    --card-light: #f7f7f7;
    --brand-purple: #6a35a6;
    --purple-soft: #8f62c4;
    --ink: #1f1f1f;
    --ink-muted: #3a3a3a;
    --mark-grey: #4a4a4c;
  }
  * { margin: 0; padding: 0; box-sizing: border-box; }
  html, body {
    width: 1200px;
    height: 900px;
    overflow: hidden;
    background: var(--stage);
  }
  .stage {
    width: 1200px;
    height: 900px;
    display: flex;
    flex-direction: column;
    align-items: center;
    justify-content: center;
    gap: 40px;
  }
  .card {
    width: 630px;
    height: 360px;
    border-radius: 28px;
    position: relative;
  }

  /* Front side */
  .card--front {
    background: var(--card-dark);
    display: flex;
    flex-direction: column;
    align-items: center;
    justify-content: center;
    gap: 26px;
  }
  .front-dot {
    width: 130px;
    height: 130px;
    border-radius: 50%;
    background: var(--brand-purple);
  }
  .front-wordmark {
    font-family: "Montserrat", sans-serif;
    font-weight: 800;
    font-size: 48px;
    color: var(--mark-grey);
    letter-spacing: 0.5px;
  }

  /* Back side */
  .card--back {
    background: var(--card-light);
    display: flex;
    align-items: center;
    padding: 0 0 0 64px;
  }
  .back-brand {
    width: 170px;
    display: flex;
    flex-direction: column;
    align-items: center;
    gap: 14px;
  }
  .back-dot {
    width: 96px;
    height: 96px;
    border-radius: 50%;
    background: var(--brand-purple);
  }
  .back-wordmark {
    font-family: "Montserrat", sans-serif;
    font-weight: 800;
    font-size: 30px;
    color: var(--ink-muted);
  }
  .divider {
    width: 2px;
    height: 156px;
    background: var(--brand-purple);
    margin: 0 30px 0 24px;
  }
  .details { display: flex; flex-direction: column; }
  .person-name {
    font-family: "Montserrat", sans-serif;
    font-weight: 700;
    font-size: 26px;
    color: var(--ink);
    line-height: 1.1;
  }
  .person-title {
    font-family: "Montserrat", sans-serif;
    font-weight: 400;
    font-size: 15px;
    color: var(--purple-soft);
    margin-bottom: 22px;
  }
  .contact-list { list-style: none; display: flex; flex-direction: column; gap: 10px; }
  .contact-item {
    display: flex;
    align-items: center;
    gap: 14px;
    font-family: "Open Sans", sans-serif;
    font-size: 16px;
    color: var(--ink);
  }
  .contact-icon { width: 16px; height: 16px; flex: none; }
</style>
</head>
<body>
  <main class="stage">
    <section class="card card--front">
      <div class="front-dot"></div>
      <div class="front-wordmark">Quolvex</div>
    </section>

    <section class="card card--back">
      <div class="back-brand">
        <div class="back-dot"></div>
        <div class="back-wordmark">Quolvex</div>
      </div>
      <div class="divider"></div>
      <div class="details">
        <div class="person-name">Your Name</div>
        <div class="person-title">Job Title</div>
        <ul class="contact-list">
          <li class="contact-item">
            <svg class="contact-icon" viewBox="0 0 16 16"><rect x="4" y="1" width="8" height="14" rx="1.5" fill="none" stroke="var(--brand-purple)" stroke-width="1.6"/><circle cx="8" cy="12.3" r="0.9" fill="var(--brand-purple)"/></svg>
            <span>000 000 0000</span>
          </li>
          <li class="contact-item">
            <svg class="contact-icon" viewBox="0 0 16 16"><rect x="1" y="3" width="14" height="10" rx="1" fill="var(--brand-purple)"/><path d="M1.5 3.6 L8 9 L14.5 3.6" fill="none" stroke="var(--card-light)" stroke-width="1.2"/></svg>
            <span>youremail@xyz.com</span>
          </li>
          <li class="contact-item">
            <svg class="contact-icon" viewBox="0 0 16 16" fill="none" stroke="var(--brand-purple)" stroke-width="1.2"><circle cx="8" cy="8" r="6.5"/><ellipse cx="8" cy="8" rx="3" ry="6.5"/><line x1="1.5" y1="8" x2="14.5" y2="8"/></svg>
            <span>www.yourwebsite.com</span>
          </li>
        </ul>
      </div>
    </section>
  </main>
</body>
</html>
```